Peer-to-peer Car Rental Business needs a business card design

We need a business card design for a new company based in Melbourne, Australia called "Wheelnest". We enable car owners to earny money by renting out their car to others in the community/neighbourhood when their not using it.
We would like to see designs that use the colour/s blue and/or orange.
The design should communicate young, modern, fun etc.
The themes to use should be community/neighbourhood, cars, parking, airports, car rental, sharing.

Our current logo is attached.

Target Market(s)

Young adults aged 20-35, travellers, environmentally conscious, cost conscious.

Industry/Entity Type

Business

Requirements
Must have
• Must have fields for persons name, title, mobile number, email company website.

```html
<!DOCTYPE html>
<html lang="en">
<head>
<meta charset="UTF-8">
<title>Wheelnest Business Card</title>
<link rel="stylesheet" href="https://fonts.googleapis.com/css2?family=Arimo:wght@400&family=Tinos:wght@700&display=swap">
<style>
  :root {
    --peach: #f9c99c;
    --plum: #921c74;
    --sun: #f6e51a;
    --brand-blue: #3c5ea9;
    --ink: #111111;
    --canvas: #ffffff;
  }
  * { margin: 0; padding: 0; box-sizing: border-box; }
  html, body {
    width: 797px;
    height: 1200px;
    overflow: hidden;
    background: var(--canvas);
  }
  .canvas {
    position: relative;
    width: 797px;
    height: 1200px;
  }
  .card {
    position: absolute;
    width: 759px;
    background: var(--peach);
    overflow: hidden;
  }
  .card--front { left: 0; top: 21px; height: 421px; }
  .card--back { left: 38px; top: 755px; height: 437px; }
  .card__shape {
    position: absolute;
    inset: 0;
    width: 100%;
    height: 100%;
  }
  .card__shape path { fill: var(--plum); }

  .brand {
    position: absolute;
    text-align: right;
    z-index: 1;
  }
  .brand__name {
    display: block;
    font-family: "Arimo", sans-serif;
    font-weight: 400;
    color: var(--brand-blue);
    letter-spacing: 0.5px;
    line-height: 1;
  }
  .brand__city {
    display: block;
    font-family: "Tinos", serif;
    font-weight: 700;
    color: var(--ink);
    line-height: 1;
  }
  .card--front .brand { right: 46px; top: 12px; }
  .card--front .brand__name { font-size: 80px; }
  .card--front .brand__city { font-size: 28px; margin-top: 22px; }
  .card--back .brand { right: 52px; top: 10px; }
  .card--back .brand__name { font-size: 50px; }
  .card--back .brand__city { font-size: 16px; margin-top: 10px; }

  .headline {
    position: absolute;
    left: 21px;
    top: 282px;
    font-family: "Tinos", serif;
    font-weight: 700;
    font-size: 57px;
    color: var(--sun);
    letter-spacing: 0.5px;
    line-height: 1;
  }

  .fields {
    position: absolute;
    left: 25px;
    top: 116px;
    list-style: none;
    font-family: "Arimo", sans-serif;
    font-size: 29px;
    color: var(--ink);
    z-index: 1;
  }
  .field {
    display: flex;
    align-items: flex-end;
    height: 46px;
  }
  .field__label { white-space: pre; }
  .field__blank {
    flex: 1;
    border-bottom: 2px solid var(--ink);
    margin-left: 6px;
    margin-bottom: 4px;
  }
  .field--long { width: 594px; }
  .field--site { width: 530px; }
  .field--extra { width: 410px; height: 50px; }
  .field--extra .field__blank { margin-left: 0; }
</style>
</head>
<body>
<main class="canvas">
  <section class="card card--front" aria-label="Business card front">
    <svg class="card__shape" viewBox="0 0 759 421" preserveAspectRatio="none" aria-hidden="true">
      <path d="M0 0 L759 421 L0 421 Z"/>
    </svg>
    <div class="brand">
      <span class="brand__name">wheelnest</span>
      <span class="brand__city">Melbourne, Australia</span>
    </div>
    <h1 class="headline">CAR FOR RENT</h1>
  </section>

  <section class="card card--back" aria-label="Business card back">
    <svg class="card__shape" viewBox="0 0 759 437" preserveAspectRatio="none" aria-hidden="true">
      <path d="M759 70 C712 78 700 130 685 190 C670 250 655 300 600 345 C520 405 300 425 0 437 L759 437 Z"/>
    </svg>
    <div class="brand">
      <span class="brand__name">wheelnest</span>
      <span class="brand__city">Melbourne, Australia</span>
    </div>
    <ul class="fields">
      <li class="field field--long"><span class="field__label">Name :</span><span class="field__blank"></span></li>
      <li class="field field--long"><span class="field__label">Title    :</span><span class="field__blank"></span></li>
      <li class="field field--long"><span class="field__label">Mobile number :</span><span class="field__blank"></span></li>
      <li class="field field--long"><span class="field__label">E-mail :</span><span class="field__blank"></span></li>
      <li class="field field--site"><span class="field__label">Company website :</span><span class="field__blank"></span></li>
      <li class="field field--extra"><span class="field__blank"></span></li>
    </ul>
  </section>
</main>
</body>
</html>
```